Security Warning Sign

We have an existing sign that needs an update. I have attached a picture of the current square sign. We need to maintain the same wording. It needs to be professional and appropriate to attach to our customers fence. Also attached is a copy of our building sign which may lend some inspiration and hopefully the ai format will assist. The final sign will be 600mm x 600mmOur website is www.halvorngate.com.au

```html
<!DOCTYPE html>
<html lang="en">
<head>
<meta charset="utf-8">
<title>Warning – Electronic Surveillance</title>
<link href="https://fonts.googleapis.com/css2?family=Montserrat:wght@500;600;800&display=swap" rel="stylesheet">
<style>
  :root {
    --bg-dark: #1d1d1e;
    --bg-mid: #2c2c2e;
    --alert-red: #e8262a;
    --text-white: #f4f4f4;
    --accent-orange: #f7931e;
  }
  * { margin: 0; padding: 0; box-sizing: border-box; }
  html, body { width: 1200px; height: 1198px; overflow: hidden; background: var(--bg-dark); }
  .sign {
    position: relative;
    width: 1200px;
    height: 1198px;
    overflow: hidden;
    font-family: "Montserrat", sans-serif;
  }
  .sign__backdrop {
    position: absolute;
    inset: 0;
    background:
      radial-gradient(ellipse at 30% 20%, var(--bg-mid) 0%, transparent 60%),
      radial-gradient(ellipse at 80% 75%, #262628 0%, transparent 55%),
      var(--bg-dark);
  }
  .sign__headline {
    position: absolute;
    top: 88px;
    left: 0;
    width: 100%;
    text-align: center;
    font-weight: 800;
    font-size: 128px;
    line-height: 1;
    letter-spacing: 2px;
    color: var(--alert-red);
    text-shadow: 4px 5px 0 rgba(0,0,0,0.55);
  }
  .sign__message {
    position: absolute;
    top: 336px;
    left: 0;
    width: 100%;
    text-align: center;
    font-weight: 500;
    font-size: 84px;
    line-height: 107px;
    color: var(--text-white);
    text-shadow: 4px 5px 0 rgba(0,0,0,0.6);
  }
  .brand {
    position: absolute;
    left: 91px;
    top: 994px;
    display: flex;
    align-items: center;
    gap: 18px;
  }
  .brand__dot {
    width: 62px;
    height: 62px;
    border-radius: 50%;
    background: var(--accent-orange);
  }
  .brand__name {
    font-weight: 800;
    font-size: 44px;
    color: var(--text-white);
    letter-spacing: 1px;
  }
  .contact-bar {
    position: absolute;
    left: 568px;
    top: 1003px;
    width: 632px;
    height: 112px;
  }
  .contact-bar__phone {
    position: absolute;
    left: 668px;
    top: 1003px;
    height: 112px;
    display: flex;
    align-items: center;
    gap: 16px;
    font-weight: 600;
    font-size: 48px;
    color: var(--text-white);
  }
  .contact-bar__icon { width: 44px; height: 44px; }
</style>
</head>
<body>
  <main class="sign">
    <div class="sign__backdrop" role="img" aria-label="Dark charcoal low-poly faceted background"></div>

    <h1 class="sign__headline">WARNING</h1>

    <p class="sign__message">
      ELECTRONIC<br>
      SURVEILLANCE<br>
      AND RECORDING<br>
      DEVICES INSTALLED<br>
      IN THIS AREA
    </p>

    <div class="brand">
      <span class="brand__dot"></span>
      <span class="brand__name">HALVORNGATE</span>
    </div>

    <svg class="contact-bar" viewBox="0 0 632 112" aria-hidden="true">
      <polygon points="30,0 48,0 18,112 0,112" fill="#f7931e"/>
      <polygon points="64,0 632,0 632,112 34,112" fill="#f7931e"/>
    </svg>

    <div class="contact-bar__phone">
      <svg class="contact-bar__icon" viewBox="0 0 24 24" aria-hidden="true">
        <path fill="#f4f4f4" d="M6.6 10.8a15.1 15.1 0 0 0 6.6 6.6l2.2-2.2a1 1 0 0 1 1-.25 11.4 11.4 0 0 0 3.6.57 1 1 0 0 1 1 1V20a1 1 0 0 1-1 1A17 17 0 0 1 3 4a1 1 0 0 1 1-1h3.5a1 1 0 0 1 1 1c0 1.25.2 2.45.57 3.57a1 1 0 0 1-.25 1z"/>
      </svg>
      <span>1300 555 018</span>
    </div>
  </main>
</body>
</html>
```